Driver License Monitoring Application Marketing Website

We need a new web design for our web application. The product is called "PermitSentry." We provide a driver license monitoring service to companies and local government bodies with driver fleets. Our current website is available at www.PermitSentry-demo.net.

I prefer a clean, single-page design with good SEO. Attached are some PDFs with data about the project.

Target Market(s)

Companies with driver fleets, local government.

Industry/Entity Type

Government

Coding

Coded - Design and coding required

Number of Pages Required

1 page

Colors
000000

Requirements
Must have
• Content from current www.PermitSentry-demo.net and attached PDFs.
Nice to have
• Prefer a simple Bootstrap or similar design for easy editing.
• Room for a simple video explanation of how the product works (we don't have an actual video yet)

```html
<!DOCTYPE html>
<html lang="en">
<head>
<meta charset="utf-8">
<title>PermitSentry – Florida Driver License Monitoring</title>
<link rel="stylesheet" href="https://fonts.googleapis.com/css2?family=Source+Sans+3:wght@300;400;700&family=Libre+Baskerville:ital@0;1&family=Montserrat:wght@400;600&family=Lato:wght@400;700&display=swap">
<style>
  :root {
    --ink: #2f3338;
    --muted: #6b6f74;
    --accent: #b3202a;
    --link: #29a9e0;
    --line: #d9dadc;
    --white: #ffffff;
    --hero-top: #3d4146;
    --hero-bottom: #2a2c2f;
  }
  * { margin: 0; padding: 0; box-sizing: border-box; }
  html, body { width: 670px; height: 1200px; overflow: hidden; background: var(--white); }
  body { position: relative; font-family: "Lato", sans-serif; color: var(--ink); }

  .hero {
    position: absolute; left: 0; top: 0; width: 670px; height: 474px;
    background: linear-gradient(180deg, var(--hero-top), #4a4d50 45%, var(--hero-bottom));
  }
  .hero-photo { position: absolute; inset: 0; }
  .site-nav { position: absolute; left: 0; top: 0; width: 670px; height: 60px; }
  .brand {
    position: absolute; left: 56px; top: 22px;
    font-family: "Source Sans 3", sans-serif; font-weight: 700; font-size: 15px;
    color: var(--white); letter-spacing: 0.3px;
  }
  .nav-links { position: absolute; top: 26px; list-style: none; }
  .nav-links li {
    position: absolute; white-space: nowrap;
    font-family: "Montserrat", sans-serif; font-size: 7.2px; letter-spacing: 1px;
    color: var(--white);
  }
  .search-btn {
    position: absolute; left: 600px; top: 22px; width: 17px; height: 17px;
    border: 1px solid var(--white); border-radius: 50%;
  }
  .search-btn svg { position: absolute; left: 4px; top: 4px; }

  .hero-copy { position: absolute; left: 0; top: 0; width: 670px; text-align: center; color: var(--white); }
  .hero-rule { position: absolute; left: 323px; top: 136px; width: 25px; height: 2px; background: var(--accent); }
  .hero-kicker {
    position: absolute; left: 0; top: 149px; width: 670px;
    font-family: "Libre Baskerville", serif; font-style: italic; font-size: 8.5px;
  }
  .hero-title {
    position: absolute; left: 0; top: 172px; width: 670px;
    font-family: "Source Sans 3", sans-serif; font-weight: 300; font-size: 37px; line-height: 48px;
  }
  .hero-sub {
    position: absolute; left: 0; top: 289px; width: 670px;
    font-family: "Libre Baskerville", serif; font-size: 12px; line-height: 19px;
  }
  .hero-btn {
    position: absolute; left: 280px; top: 369px; width: 106px; height: 19px;
    border-radius: 10px; background: var(--accent);
    font-family: "Montserrat", sans-serif; font-weight: 600; font-size: 5.8px; letter-spacing: 1px;
    line-height: 19px; text-align: center; color: var(--white);
  }
  .slider-arrow { position: absolute; top: 228px; }

  .intro { position: absolute; left: 0; top: 520px; width: 670px; text-align: center; }
  .intro-title {
    font-family: "Source Sans 3", sans-serif; font-weight: 700; font-size: 19px;
    letter-spacing: -0.6px; color: var(--ink);
  }
  .intro-rule { width: 83px; height: 1px; background: var(--line); margin: 9px auto 0; }
  .intro-text {
    width: 560px; margin: 18px auto 0;
    font-size: 8.6px; line-height: 14px; color: var(--muted);
  }

  .demo-screen { position: absolute; left: 58px; top: 706px; width: 232px; height: 192px; border-radius: 6px; background: linear-gradient(180deg, #dfe2e4, #eef0f1); }
  .demo-trucks { position: absolute; left: 327px; top: 745px; width: 262px; height: 116px; border-radius: 4px; background: linear-gradient(90deg, #e2541f, #f39a1c 55%, #f2b92a); }
  .demo-note { position: absolute; left: 248px; top: 675px; width: 182px; height: 50px; border-radius: 3px; background: #f1f1f1; }
  .demo-arrow { position: absolute; left: 296px; top: 700px; }

  .features { position: absolute; left: 0; top: 963px; width: 670px; }
  .feature { position: absolute; width: 160px; text-align: center; }
  .feature-icon {
    width: 53px; height: 53px; margin: 0 auto; border: 1px solid #e6e7e8; border-radius: 50%;
    display: flex; align-items: center; justify-content: center;
  }
  .feature-title {
    margin-top: 18px; font-family: "Montserrat", sans-serif; font-weight: 600;
    font-size: 8px; letter-spacing: 1.2px; color: var(--ink);
  }
  .feature-text { margin-top: 9px; font-size: 8.6px; line-height: 14.2px; color: var(--muted); }
  .feature-link {
    display: inline-flex; align-items: center; gap: 3px; margin-top: 22px;
    font-size: 6.4px; color: var(--link); text-decoration: none;
  }
</style>
</head>
<body>

<header class="hero">
  <div class="hero-photo" role="img" aria-label="Aerial photograph of a parked fleet of fire engines, ambulances and service trucks"></div>

  <nav class="site-nav">
    <div class="brand">PermitSentry</div>
    <ul class="nav-links">
      <li style="left:277px">HOME</li>
      <li style="left:324px">LICENSE MONITORING</li>
      <li style="left:441px">ABOUT</li>
      <li style="left:493px">CONTACT</li>
      <li style="left:555px">LOGIN</li>
    </ul>
    <div class="search-btn">
      <svg width="9" height="9" viewBox="0 0 9 9"><circle cx="3.8" cy="3.8" r="2.3" fill="none" stroke="#fff" stroke-width="1.2"/><line x1="5.5" y1="5.5" x2="7.5" y2="7.5" stroke="#fff" stroke-width="1.3"/></svg>
    </div>
  </nav>

  <svg class="slider-arrow" style="left:19px" width="14" height="22" viewBox="0 0 14 22"><polyline points="12,1 2,11 12,21" fill="none" stroke="rgba(255,255,255,.55)" stroke-width="1.4"/></svg>
  <svg class="slider-arrow" style="left:637px" width="14" height="22" viewBox="0 0 14 22"><polyline points="2,1 12,11 2,21" fill="none" stroke="rgba(255,255,255,.55)" stroke-width="1.4"/></svg>

  <div class="hero-copy">
    <div class="hero-rule"></div>
    <p class="hero-kicker">Monitor your fleet electronically</p>
    <h1 class="hero-title">Florida Driver<br>License Monitoring</h1>
    <p class="hero-sub">Get alerts by Email and Online.<br>Never let another unlicensed or unauthorized driver behind the wheel.</p>
    <div class="hero-btn">MORE INFORMATION</div>
  </div>
</header>

<section class="intro">
  <h2 class="intro-title">Monitor your drivers electronically, twenty-four hours a day.</h2>
  <div class="intro-rule"></div>
  <p class="intro-text">How many of your drivers currently have a suspended license? The answer may surprise you. Driving with a suspended license is the most commonly committed offense in America. In 2011, over 1.8 million licenses got suspended in Florida. With just over 15 million drivers, that’s 12% of all licensed Florida drivers.</p>
</section>

<div class="demo-note" role="img" aria-label="Handwritten note: check out how it works!"></div>
<svg class="demo-arrow" width="70" height="50" viewBox="0 0 70 50">
  <path d="M64 46 C60 22 40 10 12 12" fill="none" stroke="var(--accent)" stroke-width="1.3"/>
  <polyline points="18,6 10,12 18,17" fill="none" stroke="var(--accent)" stroke-width="1.3"/>
</svg>
<div class="demo-screen" role="img" aria-label="Desktop computer showing the monitoring dashboard with a play button for the explainer video, with keyboard, mouse and coffee mug"></div>
<div class="demo-trucks" role="img" aria-label="Three semi-truck cabs in red, orange and yellow"></div>

<section class="features">
  <div class="feature" style="left:69px">
    <div class="feature-icon">
      <svg width="20" height="18" viewBox="0 0 20 18"><rect x="1" y="1" width="18" height="12" rx="1" fill="none" stroke="#3a3d41" stroke-width="2"/><rect x="8" y="13" width="4" height="3" fill="#3a3d41"/><rect x="5" y="16" width="10" height="1.6" fill="#3a3d41"/></svg>
    </div>
    <h3 class="feature-title">LICENSE MONITORING</h3>
    <p class="feature-text">Monitor your fleet electronically. Get alerts by email and online. Never let another unlicensed or unauthorized driver behind the wheel.</p>
    <a class="feature-link" href="#">Understand more <svg width="8" height="8" viewBox="0 0 8 8"><circle cx="4" cy="4" r="3.4" fill="none" stroke="var(--link)" stroke-width=".8"/><polyline points="3.3,2.5 4.8,4 3.3,5.5" fill="none" stroke="var(--link)" stroke-width=".8"/></svg></a>
  </div>
  <div class="feature" style="left:255px">
    <div class="feature-icon">
      <svg width="22" height="16" viewBox="0 0 22 16"><path d="M5 2 H17 L20 8 V14 H2 V8 Z" fill="#3a3d41"/><path d="M6.5 3.5 H15.5 L17.5 7.5 H4.5 Z" fill="#fff"/><circle cx="6" cy="10.5" r="1.5" fill="#fff"/><circle cx="16" cy="10.5" r="1.5" fill="#fff"/><rect x="3" y="14" width="3" height="2" fill="#3a3d41"/><rect x="16" y="14" width="3" height="2" fill="#3a3d41"/></svg>
    </div>
    <h3 class="feature-title">PRIVATE SECTOR</h3>
    <p class="feature-text">Monitor your fleet electronically. Get alerts by email and online. Never let another unlicensed or unauthorized driver behind the wheel.</p>
    <a class="feature-link" href="#">Understand more <svg width="8" height="8" viewBox="0 0 8 8"><circle cx="4" cy="4" r="3.4" fill="none" stroke="var(--link)" stroke-width=".8"/><polyline points="3.3,2.5 4.8,4 3.3,5.5" fill="none" stroke="var(--link)" stroke-width=".8"/></svg></a>
  </div>
  <div class="feature" style="left:440px">
    <div class="feature-icon">
      <svg width="22" height="20" viewBox="0 0 22 20"><polygon points="11,1 21,6 1,6" fill="#3a3d41"/><rect x="2" y="7" width="18" height="1.6" fill="#3a3d41"/><rect x="4" y="9" width="2.2" height="7" fill="#3a3d41"/><rect x="8.3" y="9" width="2.2" height="7" fill="#3a3d41"/><rect x="12.6" y="9" width="2.2" height="7" fill="#3a3d41"/><rect x="16.4" y="9" width="2.2" height="7" fill="#3a3d41"/><rect x="1" y="17" width="20" height="2" fill="#3a3d41"/></svg>
    </div>
    <h3 class="feature-title">PUBLIC SECTOR</h3>
    <p class="feature-text">Monitor your fleet electronically. Get alerts by email and online. Never let another unlicensed or unauthorized driver behind the wheel.</p>
    <a class="feature-link" href="#">Understand more <svg width="8" height="8" viewBox="0 0 8 8"><circle cx="4" cy="4" r="3.4" fill="none" stroke="var(--link)" stroke-width=".8"/><polyline points="3.3,2.5 4.8,4 3.3,5.5" fill="none" stroke="var(--link)" stroke-width=".8"/></svg></a>
  </div>
</section>

</body>
</html>
```